Brightfield Sunray Panel cleaning business needs a flyer designed.

I need a flyer design for a new company based in Los Angeles. We clean solar panels at an affordable price, we're insured, and licensed. we would like the design to include the colors Red, white, and Blue. The flyer should emphasize the importance of cleaning solar panels to maintain the warranty and add longevity to the solar panels.

```html
<!DOCTYPE html>
<html lang="en">
<head>
<meta charset="UTF-8">
<title>Brightfield Sunray Panel Cleaning Flyer</title>
<link href="https://fonts.googleapis.com/css2?family=Russo+One&family=Poppins:ital,wght@0,500;0,600;0,700;1,800&family=Oswald:wght@600&family=Roboto+Condensed:wght@800&display=swap" rel="stylesheet">
<style>
  :root{
    --red:#c8202a;
    --navy:#0f3a8c;
    --deep:#13357f;
    --yellow:#ffe21a;
    --white:#ffffff;
    --ink:#222a3a;
  }
  *{margin:0;padding:0;box-sizing:border-box}
  html,body{width:966px;height:1200px;overflow:hidden;background:#fff}
  .flyer{position:relative;width:966px;height:1200px;overflow:hidden;font-family:"Poppins",sans-serif;color:var(--ink)}
  .hero-photo{position:absolute;left:0;top:0;width:966px;height:760px;
    background:linear-gradient(180deg,#1747d6 0%,#3f7fe0 18%,#9cc1e6 34%,#f3d9a8 46%,#e6b680 54%,#9b8a7a 62%,#6f6660 78%,#b9a998 100%)}
  .shape-layer{position:absolute;left:0;top:0}
  .brand{position:absolute;top:74px;left:0;width:966px;text-align:center;
    font-family:"Poppins",sans-serif;font-weight:700;font-size:30px;letter-spacing:3px;color:var(--white)}
  .brand-sub{position:absolute;top:112px;left:0;width:966px;text-align:center;
    font-family:"Poppins",sans-serif;font-weight:700;font-size:11px;letter-spacing:9px;color:var(--white)}
  .headline{position:absolute;left:0;width:966px;text-align:center;font-family:"Russo One",sans-serif;font-style:italic;line-height:1}
  .headline.line-1{top:140px;font-size:34px;color:var(--red);letter-spacing:2px}
  .headline.line-2{top:178px;font-size:68px;color:var(--deep)}
  .headline.line-3{top:244px;font-size:66px;color:var(--red)}
  .bubble{position:absolute;left:80px;top:531px;width:368px;height:114px;background:var(--red);border-radius:22px;padding:14px 0 0 34px;
    color:#fff;font-weight:800;font-style:italic;font-size:23px;line-height:30px}
  .bubble::after{content:"";position:absolute;left:40px;bottom:-18px;border-left:14px solid transparent;border-right:10px solid transparent;border-top:20px solid var(--red)}
  .choose-panel{position:absolute;left:491px;top:740px;width:475px;height:325px}
  .seal{position:absolute;left:630px;top:490px}
  .seal-banner{position:absolute;left:624px;top:533px;width:246px;height:48px;background:var(--deep);
    font-family:"Oswald",sans-serif;font-weight:600;color:#fff;font-size:19px;display:flex;align-items:center;justify-content:center;
    clip-path:polygon(4% 0,96% 0,100% 100%,0 100%)}
  .seal-text{position:absolute;left:649px;top:588px;width:200px;text-align:center;font-family:"Roboto Condensed",sans-serif;font-weight:800;font-size:29px;line-height:28px;color:#fff}
  .seal-text .accent{color:var(--yellow)}
  .why-clean{position:absolute;left:81px;top:706px;color:var(--red);font-weight:800;font-style:italic;font-size:22px;line-height:28px}
  .benefits{position:absolute;left:81px;top:768px;list-style:none;width:400px}
  .benefit{position:relative;padding-left:50px;margin-bottom:14px}
  .benefit .icon{position:absolute;left:0;top:2px;width:40px;height:40px;border-radius:50%;background:var(--deep)}
  .benefit h3{font-size:17px;font-weight:700;color:var(--navy);line-height:20px}
  .benefit p{font-size:14px;font-weight:500;color:#222;line-height:17px}
  .choose-title{position:absolute;left:522px;top:758px;color:#fff;font-weight:800;font-style:italic;font-size:22px}
  .reasons{position:absolute;left:530px;top:810px;list-style:none}
  .reason{position:relative;padding-left:32px;height:62px}
  .reason .tick{position:absolute;left:0;top:4px}
  .reason .pill{display:inline-block;background:var(--red);color:#fff;font-weight:600;font-size:14px;padding:1px 12px;border-radius:6px;width:198px}
  .reason p{color:#fff;font-size:13px;font-weight:500;margin-top:3px}
  .bottom-photo{position:absolute;left:0;top:960px}
  .call{position:absolute;left:518px;top:1087px;color:var(--navy);font-weight:600;font-size:12.5px;line-height:15px}
  .phone{position:absolute;left:669px;top:1093px;width:243px;height:40px;border:2px solid var(--navy);border-radius:20px;
    display:flex;align-items:center;gap:10px;padding-left:8px;color:var(--red);font-weight:600;font-size:27px;letter-spacing:.5px}
  .web{position:absolute;left:510px;top:1140px;width:420px;text-align:center;font-weight:600;font-size:14.5px;color:#111}
  .web span{color:var(--red)}
</style>
</head>
<body>
<div class="flyer">
  <div class="hero-photo" role="img" aria-label="Photo: worker in hard hat and orange vest cleaning rooftop solar panels with a long squeegee at sunset"></div>

  <svg class="shape-layer" width="966" height="1200" viewBox="0 0 966 1200" aria-hidden="true">
    <defs>
      <clipPath id="below-curve">
        <path d="M0,400 C120,640 300,745 460,738 C700,728 880,620 966,484 L966,1200 L0,1200 Z"/>
      </clipPath>
    </defs>
    <path d="M0,400 C120,640 300,745 460,738 C700,728 880,620 966,484 L966,1200 L0,1200 Z" fill="#fff"/>
    <rect x="491" y="420" width="475" height="645" fill="#13357f" clip-path="url(#below-curve)"/>
    <path d="M0,392 C120,632 300,737 460,730 C700,720 880,612 966,476" fill="none" stroke="#fff" stroke-width="6"/>
    <path d="M0,404 C120,646 300,752 460,745 C700,735 880,626 966,490" fill="none" stroke="#c8202a" stroke-width="13"/>
  </svg>

  <div class="brand">BRIGHTFIELD SUNRAY</div>
  <div class="brand-sub">PANEL CLEANING</div>

  <h1>
    <span class="headline line-1">BRIGHTFIELD SUNRAY</span>
    <span class="headline line-2">PANEL</span>
    <span class="headline line-3">CLEANING</span>
  </h1>

  <div class="bubble">Keeping Your Solar<br>Investment at<br>Peak Performance!</div>

  <svg class="seal" width="240" height="240" viewBox="0 0 240 240" aria-hidden="true">
    <circle cx="120" cy="120" r="108" fill="#fff"/>
    <circle cx="120" cy="120" r="108" fill="none" stroke="#fff" stroke-width="16" stroke-linecap="round" stroke-dasharray="0 15"/>
    <circle cx="120" cy="120" r="102" fill="#c8202a"/>
    <circle cx="120" cy="120" r="102" fill="none" stroke="#c8202a" stroke-width="12" stroke-linecap="round" stroke-dasharray="0 14"/>
  </svg>
  <div class="seal-banner">Clean Panels = More Power.</div>
  <div class="seal-text"><span class="accent">BOOK YOUR</span><br>CLEANING<br>TODAY!</div>

  <h2 class="why-clean">Why Clean<br>Your Solar Panels?</h2>
  <ul class="benefits">
    <li class="benefit">
      <svg class="icon" viewBox="0 0 40 40"><circle cx="20" cy="20" r="20" fill="#13357f"/><circle cx="20" cy="20" r="7" fill="none" stroke="#fff" stroke-width="2"/><path d="M20 9v4M20 27v4M9 20h4M27 20h4" stroke="#fff" stroke-width="2"/></svg>
      <h3>MAXIMIZE EFFICIENCY</h3><p>Dust &amp; debris reduce energy output</p>
    </li>
    <li class="benefit">
      <svg class="icon" viewBox="0 0 40 40"><circle cx="20" cy="20" r="20" fill="#13357f"/><path d="M20 10l9 4v6c0 5-4 9-9 11-5-2-9-6-9-11v-6z" fill="none" stroke="#fff" stroke-width="2"/></svg>
      <h3>PROTECT YOUR INVESTMENT</h3><p>Maintain your manufacturer warranty</p>
    </li>
    <li class="benefit">
      <svg class="icon" viewBox="0 0 40 40"><circle cx="20" cy="20" r="20" fill="#13357f"/><path d="M11 28h18M13 26v-5M18 26v-8M23 26v-6M28 26v-11" stroke="#fff" stroke-width="2"/></svg>
      <h3>EXTEND LIFESPAN</h3><p>Prevent long-term damage &amp;<br>costly repairs</p>
    </li>
    <li class="benefit">
      <svg class="icon" viewBox="0 0 40 40"><circle cx="20" cy="20" r="20" fill="#13357f"/><circle cx="20" cy="18" r="8" fill="none" stroke="#fff" stroke-width="2"/><text x="20" y="22" font-size="11" font-family="Poppins,sans-serif" font-weight="700" fill="#fff" text-anchor="middle">$</text><path d="M10 29h20" stroke="#fff" stroke-width="2"/></svg>
      <h3>BOOST SAVINGS</h3><p>More power = lower energy bills</p>
    </li>
  </ul>

  <h2 class="choose-title">Why Choose Us?</h2>
  <ul class="reasons">
    <li class="reason"><svg class="tick" width="18" height="18" viewBox="0 0 18 18"><circle cx="9" cy="9" r="8" fill="#fff"/><path d="M5 9l3 3 5-6" fill="none" stroke="#13357f" stroke-width="2"/></svg><span class="pill">Licensed &amp; Insured</span><p>Professional, worry-free service</p></li>
    <li class="reason"><svg class="tick" width="18" height="18" viewBox="0 0 18 18"><circle cx="9" cy="9" r="8" fill="#fff"/><path d="M5 9l3 3 5-6" fill="none" stroke="#13357f" stroke-width="2"/></svg><span class="pill">Affordable Rates</span><p>Top-quality cleaning at budget-friendly prices</p></li>
    <li class="reason"><svg class="tick" width="18" height="18" viewBox="0 0 18 18"><circle cx="9" cy="9" r="8" fill="#fff"/><path d="M5 9l3 3 5-6" fill="none" stroke="#13357f" stroke-width="2"/></svg><span class="pill">Los Angeles Experts</span><p>Trusted by homeowners &amp; businesses</p></li>
    <li class="reason"><svg class="tick" width="18" height="18" viewBox="0 0 18 18"><circle cx="9" cy="9" r="8" fill="#fff"/><path d="M5 9l3 3 5-6" fill="none" stroke="#13357f" stroke-width="2"/></svg><span class="pill">Eco-Friendly Solutions</span><p>Safe, non-abrasive cleaning methods</p></li>
  </ul>

  <svg class="bottom-photo" width="460" height="240" viewBox="0 0 460 240" role="img" aria-label="Photo: technician in yellow safety vest scrubbing solar panels with a brush pole">
    <defs>
      <linearGradient id="panel-tone" x1="0" y1="0" x2="1" y2="1">
        <stop offset="0" stop-color="#c9d6e8"/><stop offset="0.5" stop-color="#7f95bb"/><stop offset="1" stop-color="#d9dce0"/>
      </linearGradient>
    </defs>
    <path d="M0,35 L300,160 L330,90 L460,110 L460,240 L0,240 Z" fill="url(#panel-tone)"/>
  </svg>

  <div class="call">CALL NOW FOR A<br>FREE QUOTE!</div>
  <div class="phone">
    <svg width="20" height="20" viewBox="0 0 20 20" aria-hidden="true"><circle cx="10" cy="10" r="9" fill="none" stroke="#0f3a8c" stroke-width="2"/><path d="M7 5c-1 1-1 3 1 6s4 4 5 3l1-1-2-2-1 1c-1 0-3-2-3-3l1-1-2-2z" fill="#0f3a8c"/></svg>
    555-014-2288
  </div>
  <div class="web">www.<span>brightfieldsunraypanelcleaning</span>.com</div>
</div>
</body>
</html>
```